Kitchen and cabinet shop needs new website

Dunmore Cabinets is a mid-sized, family run cabinet shop that is in the process of updating it's image after being handed over to the second generation. It's been in the business for almost 30 years and our designers have lots of experience in the design, home building and renovation industry. Our business offers free home consultations or a customer can visit our showroom to start the design process. Whether the client is a designer, home builder or homeowner we can help create the kitchen and space you're after by helping every step of the way.

The website needs to showcase our past work, (pictures to be included), show the different styles (eg. traditional, modern) and different areas of the home we can produce cabinets for. We created a new logo with Logo forge that needs to be included in the website as well as the colours. I would like 5 pages;
-Home page
-About us
-portfolio/gallery
-services
-contact us

I would like the website to have a contemporary look, nothing too busy or complicated.

I will attach some pictures with the different styles of our work I mentioned above and provide content for each job.

Target Market(s)

home owners, designer, home builders, business owners

Industry/Entity Type

Home Builder

Number of Pages Required

5+ page

Font styles to use
Sans Serif

Requirements
Must have
• home page, about us page, gallery/portfolio page-showing various pictures of our work and different styles, services page and contact us.
• Use logo and similar colours as in logo for the scheme
• more content and pictures to follow...

```html
<!DOCTYPE html>
<html lang="en">
<head>
<meta charset="utf-8">
<title>Dunmore Cabinets — Home</title>
<link href="https://fonts.googleapis.com/css2?family=Raleway:wght@400;500;700&family=Open+Sans:wght@400;600&display=swap" rel="stylesheet">
<style>
:root{
  --blue:#1f4f9c;
  --navy:#0f2c5c;
  --navy-deep:#0a1f44;
  --orange:#ee5a1f;
  --orange-light:#f47a3c;
  --ink:#222;
  --muted:#555;
  --grey-band:#f2f2f2;
  --white:#fff;
}
*{margin:0;padding:0;box-sizing:border-box}
html,body{width:899px;height:1200px;overflow:hidden;background:var(--white)}
body{position:relative;font-family:"Open Sans",sans-serif;color:var(--ink)}
.abs{position:absolute}

/* header */
.site-header{left:0;top:0;width:899px;height:76px;background:var(--white)}
.brand{left:142px;top:20px;display:flex;align-items:center;gap:7px}
.brand-mark{width:22px;height:34px;background:var(--orange)}
.brand-name{font-family:"Raleway",sans-serif;font-weight:700;font-size:15px;color:var(--blue);letter-spacing:.4px;line-height:1}
.main-nav{left:414px;top:35px;display:flex;gap:16px;font-family:"Raleway",sans-serif;font-size:10.4px;color:var(--ink)}
.main-nav .active{color:var(--blue)}

/* hero */
.hero{left:0;top:76px;width:899px;height:387px;
  background:
    linear-gradient(180deg,rgba(255,255,255,0) 0%,rgba(255,255,255,0) 55%,rgba(236,228,214,.85) 80%,rgba(226,218,204,.95) 100%),
    linear-gradient(90deg,#dfe3e6 0%,#eef0ee 10%,#cfc3a6 22%,#e9e1c8 38%,#f4ecd4 50%,#b8a58a 62%,#d9cdb0 72%,#ece2c6 86%,#ddd2b6 100%);}
.hero-arrow{width:40px;height:40px;border-radius:50%;background:rgba(255,255,255,.75);top:182px}
.hero-arrow svg{position:absolute;left:12px;top:10px}

/* about */
.about-title{left:0;top:500px;width:899px;text-align:center;font-family:"Raleway",sans-serif;font-size:18px;font-weight:400;color:var(--ink)}
.about-lead{left:0;top:534px;width:899px;text-align:center;font-family:"Raleway",sans-serif;font-size:12px;color:#444}
.about-body{left:152px;top:557px;width:596px;text-align:center;font-size:7.4px;line-height:13px;color:var(--muted)}

/* featured services */
.services-band{left:0;top:641px;width:899px;height:222px;background:var(--grey-band)}
.service-card{top:673px;width:187px;height:155px;background:var(--white);box-shadow:0 1px 3px rgba(0,0,0,.25);border-bottom:2px solid var(--blue)}
.service-photo{position:absolute;left:0;top:0;width:187px;height:84px}
.service-title{position:absolute;left:0;top:96px;width:187px;text-align:center;font-family:"Raleway",sans-serif;font-weight:400;font-size:13px;color:var(--blue)}
.service-text{position:absolute;left:14px;top:114px;width:159px;text-align:center;font-size:6.4px;line-height:10px;color:#777}
.service-pointer{position:absolute;left:86px;bottom:0}

/* portfolio */
.portfolio-band{left:0;top:863px;width:899px;height:243px;
  background:
    linear-gradient(90deg,rgba(255,255,255,.06) 0%,rgba(255,255,255,0) 30%,rgba(255,255,255,.08) 55%,rgba(0,0,0,.04) 100%),
    linear-gradient(180deg,var(--orange-light) 0%,var(--orange) 60%,#e9561c 100%)}
.portfolio-notch{left:413px;top:863px}
.portfolio-title{left:0;top:905px;width:899px;text-align:center;font-family:"Raleway",sans-serif;font-weight:400;font-size:17px;color:var(--white);letter-spacing:.3px}
.portfolio-lead{left:0;top:930px;width:899px;text-align:center;font-family:"Raleway",sans-serif;font-size:9px;color:rgba(255,255,255,.45)}
.gallery-thumb{top:966px;width:144px;height:81px;border:2px solid var(--white)}

/* footer */
.site-footer{left:0;top:1106px;width:899px;height:94px;background:linear-gradient(180deg,#184b8c 0%,var(--navy) 50%,var(--navy-deep) 100%)}
.footer-nav{left:145px;top:1126px;font-family:"Raleway",sans-serif;font-size:10px;color:var(--white)}
.footer-nav span{margin:0 4px;opacity:.9}
.footer-legal{left:145px;top:1146px;font-size:7.5px;color:rgba(255,255,255,.4)}
.footer-social{left:145px;top:1165px;display:flex;gap:9px}
.footer-social i{display:block;width:10px;height:10px;border-radius:50%;background:var(--white)}
.footer-contact{left:569px;top:1127px;font-size:7.6px;line-height:14px;color:rgba(255,255,255,.55);font-style:normal}
</style>
</head>
<body>

<header class="site-header abs">
  <div class="brand abs">
    <div class="brand-mark"></div>
    <div class="brand-name">DUNMORE CABINETS</div>
  </div>
  <nav class="main-nav abs">
    <span class="active">Home page</span>
    <span>About us</span>
    <span>Portfolio/gallery</span>
    <span>Services</span>
    <span>Contact us</span>
  </nav>
</header>

<section class="hero abs" role="img" aria-label="Bright white kitchen with granite counters, island and dining room beyond">
  <div class="hero-arrow abs" style="left:108px">
    <svg width="16" height="20" viewBox="0 0 16 20"><path d="M11 2 L4 10 L11 18" fill="none" stroke="#222" stroke-width="1.6"/></svg>
  </div>
  <div class="hero-arrow abs" style="left:752px">
    <svg width="16" height="20" viewBox="0 0 16 20"><path d="M5 2 L12 10 L5 18" fill="none" stroke="#222" stroke-width="1.6"/></svg>
  </div>
</section>

<h1 class="about-title abs">ABOUT&nbsp; DUNMORE CABINETS</h1>
<p class="about-lead abs">Lorem ipsum dolor sit amet consectetuer adipiscing elit Nam cursus Morbi ut mi Nullam enim</p>
<p class="about-body abs">Mauris vel lacus vitae felis vestibulum volutpat Etiam est nunc venenatis in tristique eu imperdiet ac nisl Cum sociis natoque penatibus et magnis dis parturient montes nascetur ridiculus mus In iaculis facilisis massa Etiam eu urna Sed porta Suspendisse quam leo molestie sed luctus quis feugiat in pede Fusce tellus Sed metus augue convallis et vehicula ut pulvinar eu ante Integer orci tellus tristique vitae consequat nec Vivamus porttitor purus nisi eleifend libero a tempus libero lectus feugiat felis Morbi diam mauris viverra in gravida eu mattis in ante Morbi eget arcu Morbi porta libero id ullamcorper nonummy nibh ligula pulvinar metus eget</p>

<section class="services-band abs"></section>

<article class="service-card abs" style="left:155px">
  <div class="service-photo" role="img" aria-label="Kitchen with dark wood cabinets" style="background:linear-gradient(90deg,#d8d6b8 0%,#a8a682 30%,#5e4330 50%,#7a5a40 65%,#c8c8a4 85%,#9d9b74 100%)"></div>
  <h2 class="service-title">FEATUERD SERVICE</h2>
  <p class="service-text">Sed porta Suspendisse quam leo molestie sed luctus quis feugiat in pede Fusce tellus Sed metus</p>
  <svg class="service-pointer" width="15" height="7"><path d="M0 7 L7.5 0 L15 7Z" fill="var(--blue)"/></svg>
</article>
<article class="service-card abs" style="left:358px">
  <div class="service-photo" role="img" aria-label="Kitchen with range hood and island" style="background:linear-gradient(90deg,#4a4d55 0%,#b9b2a2 30%,#d8d2c4 45%,#c9c3b4 60%,#7d6a58 80%,#e4ddd0 100%)"></div>
  <h2 class="service-title">FEATUERD SERVICE</h2>
  <p class="service-text">Sed porta Suspendisse quam leo molestie sed luctus quis feugiat in pede Fusce tellus Sed metus</p>
  <svg class="service-pointer" width="15" height="7"><path d="M0 7 L7.5 0 L15 7Z" fill="var(--blue)"/></svg>
</article>
<article class="service-card abs" style="left:559px">
  <div class="service-photo" role="img" aria-label="Kitchen with dark island and pendant lights" style="background:linear-gradient(180deg,#8f9894 0%,#6c7470 45%,#2a2b2e 75%,#1e1f22 100%)"></div>
  <h2 class="service-title">FEATUERD SERVICE</h2>
  <p class="service-text">Sed porta Suspendisse quam leo molestie sed luctus quis feugiat in pede Fusce tellus Sed metus</p>
  <svg class="service-pointer" width="15" height="7"><path d="M0 7 L7.5 0 L15 7Z" fill="var(--blue)"/></svg>
</article>

<section class="portfolio-band abs" role="img" aria-label="Orange-tinted kitchen interior backdrop"></section>
<svg class="portfolio-notch abs" width="42" height="15"><path d="M0 0 L21 15 L42 0Z" fill="var(--grey-band)"/></svg>
<h2 class="portfolio-title abs">PORTFOLIO/GALLERY</h2>
<p class="portfolio-lead abs">Lorem ipsum dolor sit amet consectetuer adipiscing elit Nam cursus Morbi ut mi Nullam enim</p>
<div class="gallery-thumb abs" style="left:145px;background:linear-gradient(180deg,#cfccc4 0%,#a9a69c 45%,#6e6a62 70%,#2d2b29 100%)" role="img" aria-label="White kitchen with granite island"></div>
<div class="gallery-thumb abs" style="left:299px;background:linear-gradient(180deg,#4a1c12 0%,#7a2f1e 40%,#a84c2e 70%,#b0402a 100%)" role="img" aria-label="Cherry wood kitchen cabinets"></div>
<div class="gallery-thumb abs" style="left:458px;background:linear-gradient(180deg,#eeeeea 0%,#c7c2b8 40%,#2e2a26 65%,#5a4636 100%)" role="img" aria-label="Kitchen with dark island and bar stools"></div>
<div class="gallery-thumb abs" style="left:612px;background:linear-gradient(180deg,#e6e2d6 0%,#d9d0ba 45%,#c8b894 70%,#6c5a44 100%)" role="img" aria-label="Dining room with upholstered chairs"></div>

<footer class="site-footer abs"></footer>
<nav class="footer-nav abs">Home page<span>|</span>About us<span>|</span>Portfolio/gallery<span>|</span>Services<span>|</span>Contact us</nav>
<p class="footer-legal abs">© 2015 Company Name&nbsp; All right reserved&nbsp; Term of Use</p>
<div class="footer-social abs"><i></i><i></i><i></i></div>
<address class="footer-contact abs">
  2270 Harbourview Lane, Cedarbrook, B.C. V0X 1A0<br>
  hello@dunmorecabinets.net<br>
  Phone: (555) 014-2738
</address>

</body>
</html>
```